Boutique Financial Services/Advisor Business Needs Web Design

Looking for an informational and functional web design for my Financial Services/Financial Advisement business. It should have functionality for Company name, address, phone #, "About Us", Who we are, Our Mission, Services we offer, Biographies/Photos of/about "The Team", and possibly a link to "Contact Us". Would like to see something new & exciting blended with a traditional/professional look that will appeal to those approaching retirement, as well as those younger clients that are beginning to think about planning for the future. I already have a web domain through HostMeadow, but would like this to be the design we use for that domain.
Financial Services/Financial Advisor
Coded - Design and coding required
1 page

```html
<!DOCTYPE html>
<html lang="en">
<head>
<meta charset="utf-8">
<title>Summitvale Wealth Management</title>
<link href="https://fonts.googleapis.com/css2?family=Poppins:wght@300;400;500;600;700;800&display=swap" rel="stylesheet">
<style>
:root{
  --blue:#0a84d0;
  --navy:#0f3a66;
  --navy-deep:#0c2f55;
  --green:#0b3d02;
  --gold:#8a6a0b;
  --gold-light:#c9a227;
  --ink:#111;
  --text:#333;
  --muted:#666;
  --band:#f3f0f0;
  --line:#e2e2e2;
  --icon:#6a9b6a;
}
*{box-sizing:border-box;margin:0;padding:0}
html,body{width:1200px;height:2919px;overflow:hidden;background:#fff}
body{font-family:"Poppins",sans-serif;color:var(--text)}
.page{position:relative;width:1200px;height:2919px;overflow:hidden}
.abs{position:absolute}
.brand{font-family:"Poppins",sans-serif;font-weight:600;color:var(--navy);display:flex;align-items:center;gap:8px;line-height:1.1;white-space:nowrap}
.brand .mark{width:14px;height:14px;background:var(--navy);flex:none}
/* header */
.site-header{left:0;top:0;width:1200px;height:102px}
.site-header .brand{left:52px;top:48px;font-size:14px}
.nav-link{top:49px;font-size:10.5px;font-weight:600;color:var(--ink);white-space:nowrap}
.top-contact{top:17px;height:26px;background:var(--blue);color:#fff;font-size:10.5px;display:flex;align-items:center;justify-content:center;gap:6px;white-space:nowrap}
/* hero */
.hero{left:0;top:102px;width:1200px;height:440px}
.hero-photo{position:absolute;inset:0;background:linear-gradient(120deg,#3b4450 0%,#6b7684 35%,#2d4f75 60%,#c9d2dc 100%)}
.hero-copy{position:absolute;left:0;top:30px;width:1200px;text-align:center;color:#fff}
.hero-copy .welcome{font-size:42px;font-weight:400;letter-spacing:1px;line-height:58px}
.hero-copy .name{font-size:40px;font-weight:800;color:var(--gold-light);line-height:62px;letter-spacing:1px}
.hero-copy .lead{width:570px;margin:4px auto 0;font-size:12.5px;font-weight:700;letter-spacing:2px;line-height:18px}
.btn{display:inline-flex;align-items:center;justify-content:center;color:#fff;font-size:12.5px;letter-spacing:3px;font-weight:500;white-space:nowrap}
.btn-gold{background:var(--gold)}
.btn-blue{background:var(--blue)}
.hero .btn{position:absolute;left:522px;top:300px;width:157px;height:34px}
.hero-wave{position:absolute;left:0;top:360px;width:1200px;height:80px}
/* who */
.who-photo{left:60px;top:563px;width:428px;height:215px;background:linear-gradient(135deg,#cfd6de,#8a96a4 55%,#2d3a4a);border-top:14px solid #c5ccd4}
.section-title{font-weight:600;font-size:21px;color:var(--ink)}
.section-title em{font-style:normal;color:var(--blue)}
.who-title{left:540px;top:597px}
.body-copy{font-size:10.2px;line-height:16px;text-align:justify;color:var(--ink);font-weight:300}
.who-copy{left:540px;top:632px;width:572px}
.who-btn{left:540px;top:704px;width:171px;height:34px}
/* mission */
.mission{left:0;top:795px;width:1193px;height:413px;background:var(--band)}
.mission-title{left:52px;top:838px;color:var(--blue);font-size:21px;font-weight:600}
.mission-copy{left:52px;top:890px;width:601px;text-indent:42px}
.pill{left:52px;width:488px;height:42px;border-radius:21px;background:var(--green);color:#fff;display:flex;align-items:center;gap:12px;padding-left:10px;font-size:10px;font-weight:600;white-space:nowrap}
.pill .tick{width:30px;height:30px;border-radius:50%;border:2px solid #fff;display:flex;align-items:center;justify-content:center}
.mission-btn{left:52px;top:1140px;width:162px;height:35px}
.collage-frame{background:#fff;box-shadow:0 1px 4px rgba(0,0,0,.15);padding:8px}
.collage-frame div{width:100%;height:100%}
/* services */
.center-title{left:0;width:1200px;text-align:center}
.sub{font-size:9px;color:var(--ink)}
.card{background:#fff;box-shadow:0 2px 14px rgba(0,0,0,.12)}
.service-card{top:1348px;width:342px;height:130px;padding:36px 26px 0}
.service-card h3{font-size:13.5px;font-weight:700;color:var(--ink);margin-bottom:2px}
.service-card p{font-size:10px;line-height:16px;color:var(--ink);font-weight:300}
.service-icon{top:1311px;width:68px;height:64px;background:#fff;box-shadow:0 1px 6px rgba(0,0,0,.1);display:flex;align-items:center;justify-content:center;z-index:2}
.rule{left:0;width:1193px;height:1px;background:var(--line)}
/* team */
.team-card{top:1746px;width:342px;height:196px;padding:78px 26px 0;text-align:center}
.team-card h3{font-size:13.5px;font-weight:600;color:var(--ink)}
.team-card .role{font-size:14px;color:var(--ink);margin-bottom:6px}
.team-card p{font-size:10px;line-height:16px;color:var(--muted);text-align:left;font-weight:300}
.portrait{top:1676px;width:144px;height:144px;border-radius:50%;z-index:2}
/* contact */
.contact-info{left:100px;top:2250px;width:320px;text-align:center;font-size:12.5px;color:var(--ink);line-height:18px;font-weight:300}
.contact-info .brand{justify-content:center;font-size:19px;margin-bottom:12px}
.contact-info b{font-weight:700}
.divider-v{left:531px;top:2117px;width:1px;height:408px;background:var(--line)}
.contact-title{left:531px;width:490px;top:2118px;text-align:center;font-size:21px;font-weight:600;color:var(--ink)}
.label{left:557px;font-size:12.5px;color:var(--ink)}
.field{left:669px;width:361px;height:40px;border:1px solid #ccc;border-radius:3px;font-size:11.5px;color:#888;padding:11px 10px;background:#fff}
.submit{left:669px;top:2499px;width:172px;height:24px;background:#071b10;color:#fff;font-size:11.5px;display:flex;align-items:center;justify-content:center}
/* footer */
.footer-wave{left:0;top:2600px;width:1200px;height:140px}
.footer{left:0;top:2730px;width:1193px;height:189px;background:var(--navy)}
.footer-logo{left:137px;top:2746px;width:172px;height:86px;background:#fff;display:flex;align-items:center;justify-content:center}
.footer-logo .brand{font-size:14px}
.footer h4{font-size:14px;font-weight:600;color:#fff}
.footer-col{top:2752px;color:#fff;font-size:9px;line-height:13px}
.footer-col h4{margin-bottom:10px;font-size:14px;font-weight:600}
.footer-col .lines{font-size:8.5px;line-height:12.5px;white-space:nowrap}
.menu-links{font-size:10px;line-height:18px}
.social{display:flex;gap:16px;margin-top:16px}
.social span{width:26px;height:26px;border-radius:50%;background:#fff}
</style>
</head>
<body>
<div class="page">

  <header class="site-header abs">
    <div class="brand abs"><span class="mark"></span>Summitvale Wealth</div>
    <span class="nav-link abs" style="left:389px">About Us</span>
    <svg class="abs" style="left:448px;top:49px" width="8" height="12" viewBox="0 0 8 12"><path d="M1 1l5 5-5 5" fill="none" stroke="#111" stroke-width="2"/></svg>
    <span class="nav-link abs" style="left:496px">Services we offer</span>
    <span class="nav-link abs" style="left:602px">Our The Team</span>
    <span class="nav-link abs" style="left:709px">Contact Us</span>
    <div class="top-contact abs" style="left:908px;width:109px">
      <svg width="10" height="10" viewBox="0 0 24 24"><path fill="#fff" d="M6.6 10.8a15.1 15.1 0 006.6 6.6l2.2-2.2c.3-.3.7-.4 1-.2 1.1.4 2.3.6 3.6.6.6 0 1 .4 1 1V20c0 .6-.4 1-1 1A17 17 0 013 4c0-.6.4-1 1-1h3.5c.6 0 1 .4 1 1 0 1.3.2 2.5.6 3.6.1.3 0 .7-.2 1z"/></svg>+00 5550 1842</div>
    <div class="top-contact abs" style="left:1034px;width:124px">
      <svg width="11" height="9" viewBox="0 0 22 16"><rect width="22" height="16" rx="2" fill="#fff"/><path d="M1 1l10 8 10-8" fill="none" stroke="#0a84d0" stroke-width="2"/></svg>mail@svwm.net</div>
  </header>

  <section class="hero abs">
    <div class="hero-photo" role="img" aria-label="Photo of a businessman reviewing financial charts beside a keyboard"></div>
    <div class="hero-copy">
      <div class="welcome">Welcome to</div>
      <div class="name">SUMMITVALE WEALTH<br>MANAGEMENT</div>
      <p class="lead">Lorem ipsum dolor sit amet consectetur adipisicing elit. Molestias consequatur quos sed fugiat ducimus, fuga laborum dolorum laboriosam ex! Dolorem alias sint neque consequuntur eos illum architecto maxime fugiat possimus?</p>
    </div>
    <span class="btn btn-gold">Read more</span>
    <svg class="hero-wave" viewBox="0 0 1200 80" preserveAspectRatio="none">
      <path d="M0 55 C300 -5 700 50 1200 28 L1200 80 L0 80Z" fill="#fff"/>
      <path d="M0 48 C300 -8 700 40 1200 12 L1200 28 C700 50 300 -5 0 55Z" fill="#0a84d0"/>
    </svg>
  </section>

  <div class="who-photo abs" role="img" aria-label="Photo of a smiling team of advisors in business suits at a meeting table"></div>
  <h2 class="section-title who-title abs">Who <em>We are</em></h2>
  <p class="body-copy who-copy abs">Lorem ipsum dolor sit amet, consectetur adipisicing elit. Exercitationem, porro? Praesentium minus aspernatur doloribus nulla animi excepturi unde! Delectus similique nam amet corporis debitis dolorem tenetur blanditiis. Culpa laudantium eos sed a illum molestiae adipisci iusto, aut, magnam esse quaerat saepe eligendi? Laudantium facilis placeat nemo ratione dignissimos ipsum dicta.</p>
  <span class="btn btn-blue who-btn abs">Read more</span>

  <section class="mission abs"></section>
  <h2 class="mission-title abs">Our mission</h2>
  <p class="body-copy mission-copy abs">Lorem ipsum dolor sit amet consectetur adipisicing elit. Sed aperiam in, iusto et voluptatem, quia maiores cum architecto facere blanditiis reiciendis modi explicabo tempora minima maxime dignissimos unde necessitatibus? Maxime?</p>
  <div class="pill abs" style="top:967px"><span class="tick"><svg width="14" height="11" viewBox="0 0 14 11"><path d="M1 5.5l4 4L13 1" fill="none" stroke="#fff" stroke-width="2.2"/></svg></span>Lorem ipsum dolor sit amet consectetur adipisicing elit. Sed aperiam in</div>
  <div class="pill abs" style="top:1016px"><span class="tick"><svg width="14" height="11" viewBox="0 0 14 11"><path d="M1 5.5l4 4L13 1" fill="none" stroke="#fff" stroke-width="2.2"/></svg></span>Lorem ipsum dolor sit amet consectetur adipisicing elit. Sed aperiam in</div>
  <div class="pill abs" style="top:1066px"><span class="tick"><svg width="14" height="11" viewBox="0 0 14 11"><path d="M1 5.5l4 4L13 1" fill="none" stroke="#fff" stroke-width="2.2"/></svg></span>Lorem ipsum dolor sit amet consectetur adipisicing elit. Sed aperiam in</div>
  <span class="btn btn-gold mission-btn abs">Read more</span>

  <div class="collage-frame abs" style="left:794px;top:752px;width:236px;height:295px;background:#eee"><div role="img" aria-label="Photo of glass office towers under a blue sky above a green lawn" style="background:linear-gradient(180deg,#8fc0e8 0%,#5d86a8 55%,#4c9a2e 80%,#5fb33a 100%)"></div></div>
  <div class="collage-frame abs" style="left:712px;top:865px;width:136px;height:186px"><div role="img" aria-label="Photo of a modern family house at dusk" style="background:linear-gradient(180deg,#b58aa6,#8c8a94 50%,#5b7a48)"></div></div>
  <div class="collage-frame abs" style="left:970px;top:808px;width:150px;height:243px"><div role="img" aria-label="Photo of a stock market chart on a trading screen" style="background:linear-gradient(180deg,#2a1e22,#15191f 60%,#0d2a36)"></div></div>

  <h2 class="section-title center-title abs" style="top:1252px">Our Services</h2>
  <p class="sub center-title abs" style="top:1293px">Our financial services are a sector that provides financial services</p>

  <div class="card service-card abs" style="left:52px"><h3>Investment</h3><p>Lorem ipsum dolor sit amet, consectetur adipisicing elit. Quia voluptatem facilis ipsam fugit, aliquam corrupti asperiores laborum quibusdam quidem mollitia.</p></div>
  <div class="card service-card abs" style="left:420px"><h3>Credit or financing</h3><p>Lorem ipsum dolor sit amet, consectetur adipisicing elit. Quia voluptatem facilis ipsam fugit, aliquam corrupti asperiores laborum quibusdam quidem mollitia.</p></div>
  <div class="card service-card abs" style="left:789px"><h3>Financing other</h3><p>Lorem ipsum dolor sit amet, consectetur adipisicing elit. Quia voluptatem facilis ipsam fugit, aliquam corrupti asperiores laborum quibusdam quidem mollitia.</p></div>

  <div class="service-icon abs" style="left:251px"><svg width="44" height="40" viewBox="0 0 44 40"><g fill="#6a9b6a"><ellipse cx="26" cy="8" rx="14" ry="6"/><rect x="12" y="8" width="28" height="8"/><ellipse cx="26" cy="16" rx="14" ry="6"/><ellipse cx="18" cy="22" rx="14" ry="6" stroke="#fff" stroke-width="2"/><rect x="4" y="22" width="28" height="10"/><ellipse cx="18" cy="32" rx="14" ry="6"/></g></svg></div>
  <div class="service-icon abs" style="left:620px"><svg width="44" height="44" viewBox="0 0 44 44"><path fill="#6a9b6a" d="M15 4h14l-4 8h-6zM18 12h8c9 5 14 14 14 22 0 5-4 8-9 8H13c-5 0-9-3-9-8 0-8 5-17 14-22z"/><text x="22" y="35" text-anchor="middle" font-family="Poppins,sans-serif" font-weight="700" font-size="18" fill="#fff">$</text></svg></div>
  <div class="service-icon abs" style="left:988px"><svg width="56" height="42" viewBox="0 0 56 42"><circle cx="18" cy="17" r="15" fill="#6a9b6a"/><path d="M8 28l-4 8 10-5z" fill="#6a9b6a"/><circle cx="38" cy="24" r="13" fill="#6a9b6a" stroke="#fff" stroke-width="2"/><path d="M46 33l5 7-10-4z" fill="#6a9b6a"/><text x="18" y="23" text-anchor="middle" font-family="Poppins,sans-serif" font-weight="700" font-size="17" fill="#fff">$</text></svg></div>

  <div class="rule abs" style="top:1560px"></div>

  <h2 class="section-title center-title abs" style="top:1607px;color:var(--blue)">Our team</h2>
  <p class="sub center-title abs" style="top:1641px;font-size:10px">Our financial team are a sector that provides financial team</p>

  <div class="card team-card abs" style="left:52px"><h3>Mr. Daniel Okafor</h3><div class="role">Chief financial officer (CFO)</div><p>A senior executive who oversees all financial and accounting activities, including financial planning, transaction tracking, and strategy consulting</p></div>
  <div class="card team-card abs" style="left:420px"><h3>Miss. Helena Voss</h3><div class="role">Financial analyst</div><p>Analyzes financial information and provides financial advice to companies and organizations. They use data sets like market trends.</p></div>
  <div class="card team-card abs" style="left:789px"><h3>Mis. Clara Benning</h3><div class="role">Accountant</div><p>Collects and analyzes financial data for companies or individuals. They ensure that records are complete and accurate</p></div>
  <div class="portrait abs" role="img" aria-label="Portrait photo of the chief financial officer" style="left:148px;top:1676px;height:132px;width:144px;background:radial-gradient(circle at 50% 40%,#e6e6e6,#9a9a9a)"></div>
  <div class="portrait abs" role="img" aria-label="Portrait photo of the financial analyst" style="left:516px;height:132px;background:radial-gradient(circle at 50% 40%,#d8c3a0,#6f6a63)"></div>
  <div class="portrait abs" role="img" aria-label="Portrait photo of the accountant" style="left:885px;height:132px;background:radial-gradient(circle at 50% 40%,#c9a07a,#4d5a70)"></div>

  <div class="rule abs" style="top:2024px"></div>

  <div class="contact-info abs">
    <div class="brand"><span class="mark"></span>Summitvale Wealth</div>
    <div>&#9742; +00 5550 1842</div>
    <div>&#9993; mail@svwm.net</div>
    <div>Harbour Street, Westbay NSW 2190, <b>Australia</b></div>
    <div>PO BOX 408: Ridgefield SA 5317, <b>Australia</b></div>
  </div>
  <div class="divider-v abs"></div>
  <h2 class="contact-title abs">Contact Us</h2>
  <span class="label abs" style="top:2178px">First Name</span>
  <div class="field abs" style="top:2165px">Your name..</div>
  <span class="label abs" style="top:2235px">Last Name</span>
  <div class="field abs" style="top:2223px">Your last name..</div>
  <span class="label abs" style="top:2290px">Country</span>
  <div class="field abs" style="top:2281px;color:#222;display:flex;justify-content:space-between;align-items:center;padding:0 10px">Australia<svg width="9" height="6" viewBox="0 0 9 6"><path d="M1 1l3.5 3.5L8 1" fill="none" stroke="#222" stroke-width="1.5"/></svg></div>
  <span class="label abs" style="top:2418px">Subject</span>
  <div class="field abs" style="top:2339px;height:146px">Write something..</div>
  <div class="submit abs">Submit</div>

  <svg class="footer-wave abs" viewBox="0 0 1200 140" preserveAspectRatio="none">
    <path d="M0 70 C300 20 700 110 1193 22 L1193 140 L0 140Z" fill="#0f3a66"/>
    <path d="M0 55 C300 5 700 95 1193 0 L1193 16 C700 105 300 15 0 68Z" fill="#0a84d0"/>
    <path d="M0 95 C350 60 700 130 1193 60 L1193 140 L0 140Z" fill="#0c2f55" opacity=".5"/>
  </svg>
  <footer class="footer abs"></footer>
  <div class="footer-logo abs"><div class="brand"><span class="mark"></span>Summitvale Wealth</div></div>
  <div class="footer-col abs" style="left:466px">
    <h4>Address</h4>
    <div class="lines">&#9742; +00 5550 1842<br>&#9993; mail@svwm.net<br>Harbour Street, Westbay NSW 2190,<br><b>Australia</b><br>PO BOX 408: Ridgefield SA 5317,<br><b>Australia</b></div>
  </div>
  <div class="footer-col abs" style="left:717px">
    <h4 style="font-size:15px">Menu</h4>
    <div class="menu-links">Home<br>Services<br>Our Team<br>contact Us</div>
  </div>
  <div class="footer-col abs" style="left:967px">
    <h4>Social Media</h4>
    <div class="social" aria-label="Social media links"><span></span><span></span><span></span></div>
  </div>

</div>
</body>
</html>
```